Fast growing Tech company needs redesign of Varnith's end user website!

We need to have our login screen, the dashboard, and the one page of the Varnith site to be redesigned for the end-users. Varnith is a document hosting service for title companies and real estate law firms. This allows the buyers and sellers to view their closing documents after closing along with many other features that help them out during the closing of their property. More information about what we do can be found on our test site https://qpx.482.sampledrafthost.example/. PLEASE NOTE: THE ABOVE SITE IS NOT THE ONE WE NEED REDONE. The above site is our corporate site that explains our service offering and we thought it would be helpful in providing you a better understanding of our service.
The site that we want to have redesigned is for the end user. THE SITE THAT NEEDS TO BE REDONE ARE THE SCREENSHOTS ATTACHED. We will need the login screen, dashboard, and the one page redesigned.
.
We will just need this in HTML and we will then do the rest for the placeholders for logos, data, mapping etc.
Overall, we want a new, fresh, and modern look for the website and we want the login screen, dashboard and one page website to be consistent in design. Again, these are the three screenshots that are attached.
For the winner, we will most likely need to hire you again for more sites because we have other versions.
Thank you and if any questions, please let us know.
Target Market(s)
This site is for buyer and sellers during the closing process of real estate transaction.

```html
<!DOCTYPE html>
<html lang="en">
<head>
<meta charset="utf-8">
<title>Varnith – Closing Dashboard</title>
<link href="https://fonts.googleapis.com/css2?family=Lato:wght@400;700&display=swap" rel="stylesheet">
<style>
:root{
  --blue:#1b75bb;
  --blue-dark:#135e99;
  --ink:#333;
  --muted:#777;
  --grey-bg:#eef1f4;
  --green:#17b83a;
  --grey-badge:#9a9a9a;
  --white:#fff;
  --line:#d9dde2;
}
*{box-sizing:border-box;margin:0;padding:0}
html,body{width:1200px;height:5067px;overflow:hidden;background:var(--white)}
body{font-family:'Lato',sans-serif;color:var(--ink)}
.page{position:relative;width:1200px;height:5067px}
.abs{position:absolute}
.brand{left:0;width:1200px;top:30px;text-align:center;font-size:60px;font-weight:700;color:var(--blue);letter-spacing:1px}
.hero{left:85px;top:150px;width:1028px;height:578px;background:linear-gradient(160deg,#4c5a4a 0%,#2c3a44 45%,#1d2a33 100%)}
.clients{left:673px;top:299px;width:401px;height:258px;background:var(--white);text-align:center;padding-top:44px}
.clients .label{font-size:17px;font-variant:small-caps;letter-spacing:.5px}
.clients .name{margin-top:66px;font-size:26px;color:var(--ink);font-weight:700}
.heading{display:flex;align-items:center;gap:10px;font-size:30px;font-variant:small-caps;letter-spacing:.3px;white-space:nowrap}
.heading .first{color:var(--ink)}
.heading .accent{color:var(--blue)}
.heading .rule{width:84px;height:3px;background:var(--blue);margin-left:12px}
.heading.light .first,.heading.light .accent{color:var(--white)}
.intro{left:85px;top:922px;width:428px;font-size:18.5px;line-height:31px;text-align:justify}
.map{left:641px;top:925px;width:474px;height:603px;background:linear-gradient(140deg,#6e7f5c,#8b8f7a 40%,#5e7049 75%,#7a7c6c)}
.photo{left:806px;top:1432px;width:355px;height:293px;background:linear-gradient(180deg,#3d4a55,#7d8a92 60%,#4b5550);box-shadow:0 6px 18px rgba(0,0,0,.25)}
.info{left:0;top:1186px;width:557px;height:582px;background:var(--blue);color:var(--white);padding:42px 0 0 87px}
.info h3{font-size:27px;font-variant:small-caps;font-weight:700;margin-bottom:18px}
.info p{font-size:19px;line-height:31px;padding-left:22px}
.info .group{margin-bottom:40px}
.milestones{left:0;top:1904px;width:1200px;height:909px;background:var(--grey-bg)}
.card{width:262px;height:260px;background:var(--white);box-shadow:0 1px 3px rgba(0,0,0,.06)}
.card .num{position:absolute;left:18px;top:62px;font-size:46px;color:var(--blue);font-weight:400;letter-spacing:2px}
.card .icon{position:absolute;right:18px;top:28px;width:92px;height:92px;border-radius:50%;background:#e3eef7;display:flex;align-items:center;justify-content:center}
.card .title{position:absolute;left:18px;top:134px;font-size:21px;font-variant:small-caps;line-height:30px}
.badge{position:absolute;left:18px;top:210px;padding:6px 15px;border-radius:5px;font-size:14px;color:var(--white)}
.badge.done{background:var(--green)}
.badge.todo{background:var(--grey-badge)}
.card.active{background:var(--blue)}
.card.active .num,.card.active .title{color:var(--white)}
.card.active .icon{background:var(--white)}
.card.active .badge{background:#555}
.docs{left:0;top:2813px;width:1200px;height:487px;background:var(--blue)}
.doc-link{display:flex;align-items:center;gap:28px;color:var(--white);font-size:21px;text-decoration:underline}
.wiring{left:576px;top:2923px;width:537px;height:490px;background:var(--white);box-shadow:0 4px 14px rgba(0,0,0,.12);padding:38px 40px 0}
.wiring h3{font-size:32px;font-variant:small-caps;font-weight:400}
.wiring h3 span{color:var(--blue)}
.wiring ul{list-style:none;margin-top:40px}
.wiring li{font-size:14px;font-weight:700;margin-bottom:26px}
.wiring .rule{height:1px;background:var(--line);margin-top:70px}
.wiring a{display:block;margin-top:20px;font-size:14px;color:var(--blue);text-decoration:underline}
.agent{width:318px;height:213px;background:var(--white);border:1px solid var(--line);box-shadow:0 2px 6px rgba(0,0,0,.06);padding:90px 20px 0 20px}
.agent .pic{position:absolute;left:20px;top:-71px;width:142px;height:140px;background:linear-gradient(180deg,#c9ccd2,#8a909a)}
.agent .name{color:var(--blue);font-size:20px;font-weight:700}
.agent .org{font-size:13px;color:var(--muted);margin-top:6px;padding-bottom:12px;border-bottom:1px solid var(--line)}
.agent .meta{font-size:14px;color:var(--muted);margin-top:14px;line-height:24px}
.checklist{left:85px;top:4195px;width:440px}
.big-title{font-size:36px;font-variant:small-caps}
.big-title span{color:var(--blue)}
.item{position:relative;border-bottom:1px solid var(--line);padding:20px 0 16px}
.item .t{font-size:14px;font-weight:700;width:320px;line-height:20px}
.item .s{font-size:14px;font-weight:700;color:var(--blue);margin-top:14px}
.item .box{position:absolute;right:4px;top:24px;width:20px;height:20px;background:var(--green)}
.vline{left:559px;top:4318px;width:4px;height:424px;background:#dde2e8}
.vline i{display:block;width:4px;height:100px;background:var(--blue)}
.wishlist{left:600px;top:4157px;width:513px;height:633px;background:var(--blue);padding:40px 38px 0 36px;color:var(--white)}
.wishlist .big-title{color:var(--white)}
.wishlist .item{border-color:rgba(255,255,255,.35)}
.wishlist .item .s{color:var(--white)}
.wishlist .item .box{background:none;border:2px solid var(--white)}
.add{margin-top:30px;background:var(--white);height:94px;padding:20px 18px;color:var(--ink);position:relative}
.add .t{font-size:14px;font-weight:700}
.add .field{position:absolute;left:18px;right:80px;top:64px;height:2px;background:var(--blue-dark)}
.add .btn{position:absolute;right:10px;top:46px;background:var(--blue);color:var(--white);font-size:14px;padding:7px 14px}
.cta{left:301px;top:4845px;width:572px;height:57px;background:var(--blue);color:var(--white);font-size:20px;display:flex;align-items:center;justify-content:center}
</style>
</head>
<body>
<div class="page">

  <div class="abs brand">Varnith</div>

  <div class="abs hero" role="img" aria-label="Photo of a modern dark-roofed house among pine trees with a car on the driveway"></div>
  <div class="abs clients">
    <div class="label">Our Clients</div>
    <div class="name">Brightline Law Firm</div>
  </div>

  <div class="abs heading" style="left:88px;top:830px">
    <svg width="22" height="30" viewBox="0 0 22 30"><circle cx="7" cy="8" r="5" fill="none" stroke="#1b75bb" stroke-width="2"/><path d="M7 13 q0 12 12 12" fill="none" stroke="#1b75bb" stroke-width="2"/></svg>
    <span class="first">Welcome</span><span class="accent">Dana Buyer</span><span class="rule"></span>
  </div>

  <p class="abs intro">On behalf of all of us at Brightline Law Firm, we would like to thank you for choosing us for the closing of your property. Because we want you to be informed at every step of the process, we use the innovative Digital Closing Package to keep all parties involved in the transaction on the same page for a smooth and successful closing.</p>

  <div class="abs map" role="img" aria-label="Aerial map view of the property location"></div>
  <div class="abs photo" role="img" aria-label="Photo of a modern two-storey house at dusk"></div>

  <div class="abs info">
    <div class="group">
      <h3>Your Transaction Information</h3>
      <p>File Number : 2018-015987<br>Buyer : Dana Buyer<br>Seller : Mira Seller<br>Agent : Theo Buyer Agent</p>
    </div>
    <div class="group">
      <h3>Property Address</h3>
      <p>2400 Alder Street<br>Miami, FL 33155</p>
    </div>
    <div class="group">
      <h3>Purchase Details</h3>
      <p>Purchase Price : $580,000<br>Settlement Date : Tue, Dec 25, 2020</p>
    </div>
  </div>

  <section class="abs milestones">
    <div class="abs heading" style="left:88px;top:80px">
      <svg width="22" height="30" viewBox="0 0 22 30"><circle cx="7" cy="8" r="5" fill="none" stroke="#1b75bb" stroke-width="2"/><path d="M7 13 q0 12 12 12" fill="none" stroke="#1b75bb" stroke-width="2"/></svg>
      <span class="first">Closing</span><span class="accent">Milestones</span><span class="rule"></span>
    </div>

    <div class="abs card" style="left:85px;top:181px">
      <div class="icon"><svg width="44" height="44" viewBox="0 0 44 44" fill="none" stroke="#1b75bb" stroke-width="2"><rect x="6" y="12" width="32" height="20" rx="2"/><circle cx="22" cy="22" r="6"/></svg></div>
      <div class="num">01</div><div class="title">Transaction<br>Strated</div><span class="badge done">Completed</span>
    </div>
    <div class="abs card" style="left:470px;top:181px">
      <div class="icon"><svg width="44" height="44" viewBox="0 0 44 44" fill="none" stroke="#1b75bb" stroke-width="2"><circle cx="26" cy="14" r="8"/><path d="M4 30h10l8 4h14v4H20l-8-4H4z"/></svg></div>
      <div class="num">02</div><div class="title">Earnest Money<br>Received</div><span class="badge done">Completed</span>
    </div>
    <div class="abs card active" style="left:852px;top:181px">
      <div class="icon"><svg width="44" height="44" viewBox="0 0 44 44" fill="none" stroke="#1b75bb" stroke-width="2"><rect x="10" y="6" width="22" height="32" rx="2"/><path d="M15 16h12M15 22h12M15 28h8"/></svg></div>
      <div class="num">03</div><div class="title">Delivered Title<br>Report</div><span class="badge todo">Not Completed</span>
    </div>
    <div class="abs card" style="left:85px;top:513px">
      <div class="icon"><svg width="44" height="44" viewBox="0 0 44 44" fill="none" stroke="#1b75bb" stroke-width="2"><rect x="8" y="8" width="28" height="28" rx="2"/><path d="M8 18h28M14 26h16"/></svg></div>
      <div class="num">04</div><div class="title">Title<br>Cleared</div><span class="badge todo">Not Completed</span>
    </div>
    <div class="abs card" style="left:470px;top:513px">
      <div class="icon"><svg width="44" height="44" viewBox="0 0 44 44" fill="none" stroke="#1b75bb" stroke-width="2"><path d="M10 6h18l6 6v26H10z"/><path d="M15 18h14M15 24h14M15 30h8"/></svg></div>
      <div class="num">05</div><div class="title">Signing<br>Scheduled</div><span class="badge todo">Not Completed</span>
    </div>
    <div class="abs card" style="left:852px;top:513px">
      <div class="icon"><svg width="44" height="44" viewBox="0 0 44 44" fill="none" stroke="#1b75bb" stroke-width="2"><rect x="8" y="6" width="28" height="32" rx="2"/><path d="M14 14h16M14 20h16M14 26h10"/><path d="M26 30l4 4 6-8"/></svg></div>
      <div class="num">06</div><div class="title">Transaction<br>Closed</div><span class="badge todo">Not Completed</span>
    </div>
  </section>

  <section class="abs docs">
    <div class="abs heading light" style="left:88px;top:88px">
      <svg width="22" height="30" viewBox="0 0 22 30"><circle cx="7" cy="8" r="5" fill="none" stroke="#fff" stroke-width="2"/><path d="M7 13 q0 12 12 12" fill="none" stroke="#fff" stroke-width="2"/></svg>
      <span class="first">Documents you need to view</span>
    </div>
    <a class="abs doc-link" style="left:135px;top:200px"><svg width="24" height="28" viewBox="0 0 24 28" fill="none" stroke="#fff" stroke-width="2"><rect x="2" y="2" width="20" height="24" rx="3"/><path d="M7 10h10M7 15h10M7 20h6"/></svg>Closing Paper Work</a>
    <a class="abs doc-link" style="left:135px;top:262px"><svg width="24" height="28" viewBox="0 0 24 28" fill="none" stroke="#fff" stroke-width="2"><rect x="2" y="2" width="20" height="24" rx="3"/><path d="M7 10h10M7 15h10M7 20h6"/></svg>Purchase Agreement</a>
  </section>

  <div class="abs wiring">
    <h3>Wiring <span>Instruction</span></h3>
    <ul>
      <li>BANK NAME:</li><li>BANK ADDRESS:</li><li>BANK PHONE:</li><li>BANK ABA NUMBER:</li><li>ACCOUNT NUMBER:</li><li>ANY ADDITIONAL INFORMATION:</li>
    </ul>
    <div class="rule"></div>
    <a>Download Wire Instruction Document</a>
  </div>

  <div class="abs heading" style="left:88px;top:3536px">
    <svg width="22" height="30" viewBox="0 0 22 30"><circle cx="7" cy="8" r="5" fill="none" stroke="#1b75bb" stroke-width="2"/><path d="M7 13 q0 12 12 12" fill="none" stroke="#1b75bb" stroke-width="2"/></svg>
    <span class="first">Real Estate</span><span class="accent">Agents</span><span class="rule"></span>
  </div>

  <div class="abs agent" style="left:85px;top:3747px">
    <div class="pic" role="img" aria-label="Portrait photo of the law firm contact"></div>
    <div class="name">Nora Whitfield</div><div class="org">Brightline Law Firm</div>
    <div class="meta">Email Address<br>305-555-0142</div>
  </div>
  <div class="abs agent" style="left:447px;top:3747px">
    <div class="pic" role="img" aria-label="Portrait photo of the buyer agent"></div>
    <div class="name">Theo Buyer Agent</div><div class="org">Theos Realty</div>
    <div class="meta">Email Address<br>1-780-555-0118</div>
  </div>
  <div class="abs agent" style="left:797px;top:3747px">
    <div class="pic" role="img" aria-label="Portrait photo of the loan officer"></div>
    <div class="name">Owen Loan Officer</div><div class="org">Owens Lending</div>
    <div class="meta">Email Address<br>1-305-555-0176</div>
  </div>

  <div class="abs checklist">
    <div class="big-title">Moving <span>Checklist</span></div>
    <div style="margin-top:50px">
      <div class="item"><div class="t">ADDRESS CHANGE - POST OFFICE :</div><div class="s">COMPLETED !</div><span class="box"></span></div>
      <div class="item"><div class="t">ADDRESS CHANGE - BANK :</div><div class="s">COMPLETED !</div><span class="box"></span></div>
      <div class="item"><div class="t">ADDRESS CHANGE - CREDIT CARD COMPANIES ::</div><div class="s">COMPLETED !</div><span class="box"></span></div>
      <div class="item"><div class="t">ADDRESS CHANGE - LIFE INSURANCE :</div><div class="s">COMPLETED !</div><span class="box"></span></div>
    </div>
  </div>
  <div class="abs vline"><i></i></div>

  <div class="abs wishlist">
    <div class="big-title">Moving Wishlist</div>
    <div style="margin-top:50px">
      <div class="item"><div class="t">NEED TO CALL ROOFING COMPANY :</div><div class="s">COMPLETED !</div><span class="box"></span></div>
      <div class="item"><div class="t">CALL FLOORING COMPANY :</div><div class="s">COMPLETED !</div><span class="box"></span></div>
    </div>
    <div class="add"><div class="t">ADD ITEMS TO WISHLIST</div><span class="field"></span><span class="btn">ADD</span></div>
  </div>

  <a class="abs cta">CLICK HERE TO CHANGE YOUR ADDRESS/COUPONS</a>

</div>
</body>
</html>
```